Criminal Defense Law Firm needs Stationary design Theme for a Business Card, Envelope, and Letterhea

Our Law Firm is seeking a general design concept for a business card, letterhead, and Envelope.

Our website is WillowcrestTrialDesk.com

A design for these three items is requested to keep branding in place for the firm. Would like to keep the Firm Colors on the website consistent with our branding on business cards, letterheads, and mailing envelopes #10 size to be exact.

We would like business cards printed front and back with Law firm Colors from website.

Letterhead with law firm colors as well. Design is not limited to just the header, but the footer can be utilized as well for email, website, phone, fax, etc.

Simple #10 envelope consisting of the same design principles set out in the previous two designs.

```html
<!DOCTYPE html>
<html lang="en">
<head>
<meta charset="utf-8">
<title>Willowcrest Trial Offices – Business Card</title>
<link rel="stylesheet" href="https://fonts.googleapis.com/css2?family=Cinzel:wght@500&family=Open+Sans:wght@400;600&display=swap">
<style>
  :root {
    --bg: #ece9e4;
    --ink: #1b1b1c;
    --band: #161617;
    --band-hi: #3a3a3c;
    --gold: #b39a6b;
    --blue: #1fa8c9;
    --paper: #ffffff;
    --grey: #5c5c5e;
    --rule: #c9c9c9;
  }
  html, body { margin: 0; padding: 0; }
  body {
    width: 1200px; height: 1024px; overflow: hidden;
    background: var(--bg);
    font-family: "Open Sans", Arial, sans-serif;
  }
  .card {
    position: absolute; left: 220px; width: 760px; height: 434px;
    box-shadow: 0 10px 28px rgba(0,0,0,.22);
    overflow: hidden;
  }
  .card-front { top: 56px; background: var(--paper); }
  .card-back {
    top: 532px;
    background: radial-gradient(ellipse at 40% 35%, var(--band-hi) 0%, var(--band) 70%);
  }
  .swoosh { position: absolute; inset: 0; }
  .front-web {
    position: absolute; left: 34px; top: 30px;
    font-size: 15px; color: #fff; letter-spacing: .3px;
  }
  .front-web span, .back-web span { color: var(--blue); }
  .brand { position: absolute; display: flex; align-items: center; gap: 18px; }
  .brand-dot {
    width: 54px; height: 54px; border-radius: 50%;
    border: 2px solid currentColor; box-sizing: border-box; flex: none;
  }
  .brand-name {
    font-family: "Cinzel", Georgia, serif; font-weight: 500;
    font-size: 27px; line-height: 1.05; letter-spacing: 1px; text-transform: uppercase;
  }
  .card-front .brand { left: 196px; top: 196px; color: var(--ink); }
  .person { position: absolute; left: 268px; top: 274px; font-size: 17px; font-weight: 600; }
  .person-name { color: var(--gold); }
  .person-sep { color: var(--rule); padding: 0 4px; }
  .person-title { color: var(--blue); }
  .rule { position: absolute; left: 56px; right: 40px; height: 1px; background: var(--rule); }
  .rule-top { top: 314px; }
  .rule-bottom { top: 372px; }
  .contacts {
    position: absolute; left: 60px; right: 40px; top: 330px;
    display: flex; justify-content: space-between; align-items: center;
    font-size: 13.5px; color: var(--grey);
  }
  .contact { display: flex; align-items: center; gap: 6px; }
  .contact svg { width: 16px; height: 16px; flex: none; }
  .card-back .brand { left: 150px; top: 150px; color: #fff; }
  .card-back .brand-name { font-size: 30px; }
  .back-web {
    position: absolute; left: 150px; top: 268px; font-size: 15px; color: #fff;
  }
</style>
</head>
<body>

<section class="card card-front" aria-label="Business card front">
  <svg class="swoosh" viewBox="0 0 760 434" preserveAspectRatio="none" aria-hidden="true">
    <path d="M0 0 H760 V40 C600 40 520 90 420 150 C330 200 200 196 0 200 Z" fill="var(--blue)"/>
    <path d="M0 0 H760 V22 C620 20 520 70 400 140 C300 196 180 186 0 196 Z" fill="var(--gold)"/>
    <path d="M0 0 H760 V14 C620 12 500 60 380 126 C280 178 170 170 0 176 Z" fill="var(--band)"/>
  </svg>
  <div class="front-web">www.<span>WillowcrestTrialDesk</span>.com</div>

  <div class="brand">
    <div class="brand-dot"></div>
    <div class="brand-name">Willowcrest Trial<br>Law Offices</div>
  </div>

  <div class="person">
    <span class="person-name">Marcus Hale</span><span class="person-sep">|</span><span class="person-title">Lawyer</span>
  </div>

  <div class="rule rule-top"></div>
  <div class="contacts">
    <div class="contact">
      <svg viewBox="0 0 16 16"><circle cx="8" cy="8" r="8" fill="var(--gold)"/><path d="M8 3.5a2.6 2.6 0 0 0-2.6 2.6C5.4 8.2 8 12 8 12s2.6-3.8 2.6-5.9A2.6 2.6 0 0 0 8 3.5z" fill="#fff"/></svg>
      214 Cedar Lane NW, Millbrook, NM 87000
    </div>
    <div class="contact">
      <svg viewBox="0 0 16 16"><circle cx="8" cy="8" r="8" fill="var(--gold)"/><path d="M5.4 4h1.6l.7 2-1 .8a5 5 0 0 0 2.5 2.5l.8-1 2 .7v1.6c0 .6-.5 1-1 1A7 7 0 0 1 4.4 5c0-.5.4-1 1-1z" fill="#fff"/></svg>
      505.555.0142
    </div>
    <div class="contact">
      <svg viewBox="0 0 16 16"><circle cx="8" cy="8" r="8" fill="var(--gold)"/><path d="M5.4 4h1.6l.7 2-1 .8a5 5 0 0 0 2.5 2.5l.8-1 2 .7v1.6c0 .6-.5 1-1 1A7 7 0 0 1 4.4 5c0-.5.4-1 1-1z" fill="#fff"/></svg>
      505.555.0187
    </div>
    <div class="contact">
      <svg viewBox="0 0 16 16"><circle cx="8" cy="8" r="8" fill="var(--gold)"/><rect x="4" y="5" width="8" height="6" rx="1" fill="#fff"/><path d="M4.3 5.4 8 8.3l3.7-2.9" stroke="var(--gold)" stroke-width="1" fill="none"/></svg>
      name@<span style="color:var(--blue)">WillowcrestTrialDesk</span>.com
    </div>
  </div>
  <div class="rule rule-bottom"></div>
</section>

<section class="card card-back" aria-label="Business card back">
  <div class="brand">
    <div class="brand-dot"></div>
    <div class="brand-name">Willowcrest Trial<br>Law Offices</div>
  </div>
  <div class="back-web">www.<span>WillowcrestTrialDesk</span>.com</div>
</section>

</body>
</html>
```